Kelmora Lodges internet banner add

Seldovia Alaska -I need a fabulous UNIQUE web banner for our two locations Kelmora Lodges Harbor Location and Kelmora Lodges Central location
All suites have full Kitchens
Open year Round
We cater to vacationers - fishermen - hikers - and families
Classy upbeat modern design
The dimensions for the banner ads are:

300x250
OR
728x90

Target Market(s)

Alaska- Nautical

Industry/Entity Type

Vacation rentals

Requirements
Must have
• I would like the attached photo as background Kelmora Lodges - every path brings you home with our phone number- email - and 2 websites

```html
<!DOCTYPE html>
<html lang="en">
<head>
<meta charset="utf-8">
<title>Kelmora Lodges – Web Banners</title>
<link rel="stylesheet" href="https://fonts.googleapis.com/css2?family=Josefin+Sans:wght@400&family=Great+Vibes&family=Oswald:wght@600&family=Roboto:wght@700;900&display=swap">
<style>
  :root {
    --stage: #3b413e;
    --navy: #2d4a68;
    --navy-deep: #1f3550;
    --accent-red: #c8323a;
    --phone-gold: #f3cb45;
    --white: #ffffff;
    --sky-top: #2f7fd0;
    --sky-mid: #8fc3ea;
    --sea: #2c6fa6;
    --forest: #2f4a2c;
    --forest-dark: #1a2a19;
  }
  * { margin: 0; padding: 0; box-sizing: border-box; }
  html, body { width: 1200px; height: 960px; overflow: hidden; }
  body {
    background: radial-gradient(ellipse at 50% 40%, #434a46 0%, var(--stage) 70%);
    position: relative;
    font-family: "Roboto", Arial, sans-serif;
  }
  .banner { position: absolute; overflow: hidden; }
  .banner-photo { position: absolute; inset: 0; }

  /* 300x250 banner */
  .banner-square { left: 420px; top: 156px; width: 360px; height: 300px; }
  .banner-square .banner-photo {
    background: linear-gradient(180deg, var(--sky-top) 0%, var(--sky-mid) 28%, #d9ecf8 40%, var(--sea) 52%, var(--forest) 64%, var(--forest-dark) 100%);
  }
  .brand-name {
    position: absolute;
    font-family: "Josefin Sans", Arial, sans-serif;
    font-weight: 400;
    color: var(--navy);
    text-transform: uppercase;
    white-space: nowrap;
  }
  .banner-square .brand-name {
    left: 0; right: 0; top: 62px; text-align: center;
    font-size: 29px; letter-spacing: 3px;
  }
  .brand-rule { position: absolute; height: 2px; background: var(--navy); }
  .banner-square .brand-rule { left: 24px; right: 24px; top: 102px; }
  .tagline-script {
    position: absolute; left: 0; right: 0; top: 116px; text-align: center;
    font-family: "Great Vibes", cursive;
    font-size: 33px; color: var(--navy-deep);
    text-shadow: 0 0 6px rgba(255,255,255,.9), 0 0 2px rgba(255,255,255,.9);
  }
  .phone {
    position: absolute;
    font-family: "Oswald", Arial, sans-serif; font-weight: 600;
    color: var(--phone-gold);
    text-shadow: 2px 3px 4px rgba(0,0,0,.75);
    white-space: nowrap;
  }
  .banner-square .phone { left: 0; right: 0; top: 160px; text-align: center; font-size: 40px; }
  .contact-list { position: absolute; list-style: none; color: var(--white); font-weight: 700; text-shadow: 1px 1px 3px rgba(0,0,0,.8); }
  .banner-square .contact-list { left: 0; right: 0; top: 216px; text-align: center; font-size: 15px; line-height: 21.5px; }

  /* 728x90 banner */
  .banner-wide { left: 163px; top: 587px; width: 874px; height: 107px; }
  .banner-wide .banner-photo {
    background:
      linear-gradient(90deg, rgba(240,246,250,.92) 0%, rgba(225,237,246,.85) 30%, rgba(225,237,246,0) 46%),
      linear-gradient(180deg, #a9cfee 0%, #e6f1f9 30%, var(--sea) 55%, var(--forest) 78%, var(--forest-dark) 100%);
  }
  .banner-wide .brand-name { left: 0; width: 305px; top: 46px; text-align: center; font-size: 27px; letter-spacing: 2.5px; }
  .banner-wide .brand-rule { left: 16px; width: 274px; top: 82px; }
  .tagline-caps {
    position: absolute; left: 346px; top: 20px;
    font-weight: 900; font-size: 14.5px; letter-spacing: 1px;
    color: var(--navy-deep); text-transform: uppercase;
    text-shadow: 0 0 4px rgba(255,255,255,.9);
  }
  .banner-wide .phone { left: 344px; top: 38px; font-size: 48px; line-height: 60px; }
  .banner-wide .contact-list { right: 29px; top: 42px; text-align: right; font-size: 14px; line-height: 17.5px; }
</style>
</head>
<body>
  <section class="banner banner-square" aria-label="Kelmora Lodges 300 by 250 banner">
    <div class="banner-photo" role="img" aria-label="Alaskan coastline photo: blue sky, snowy mountain across the bay and evergreen forest in the foreground"></div>
    <div class="brand-name">Kelmora Lodges</div>
    <div class="brand-rule"></div>
    <p class="tagline-script">Every path brings you home</p>
    <p class="phone">907-555-0142</p>
    <ul class="contact-list">
      <li>Kelmora_Lodges@harbormail.com</li>
      <li>CentralLodgesofKelmora.com</li>
      <li>KelmoraHarborInn.com</li>
    </ul>
  </section>

  <section class="banner banner-wide" aria-label="Kelmora Lodges 728 by 90 banner">
    <div class="banner-photo" role="img" aria-label="Panoramic Alaskan bay photo with snowy mountain and evergreen treetops"></div>
    <div class="brand-name">Kelmora Lodges</div>
    <div class="brand-rule"></div>
    <p class="tagline-caps">Every path brings you home</p>
    <p class="phone">907-555-0142</p>
    <ul class="contact-list">
      <li>Kelmora_Lodges@harbormail.com</li>
      <li>CentralLodgesofKelmora.com</li>
      <li>KelmoraHarborInn.com</li>
    </ul>
  </section>
</body>
</html>
```